Re-design of 4 x 2-sided reports

I need the 4 attached reports (3 are 2-sides of A4; 1 is 7-sides of A4) to be re-designed with a consistent look and feel. Just need 1 or 2 images per report being inserted plus consistent branding and contact details being displayed in the same location on each report with same colour, font and design). Reports are attached.
The reports are used as lead magnets.
That is, visitors to our website can download one of them (7 Steps To Sharpen Your Sales Over The Coming Month) by filling in a form with their email address. Then over the next 30 days the other reports are sent to the subscriber via email autoresponders.
Blue Harbour Marketing is a marketing consultancy dealing with companies in the North West of England providing cost-effective and profitable marketing to small and medium-sized businesses that want better and quicker results. The reports need to be professional and corporate looking. Please let me know if you need any further clarification or have any questions. I attach an example report. I don't necessarily want to mirror this report (from the law firm) but it may help to understand what look I'm trying to get. Many thanks, Gordon

Target Market(s)

SMEs based in NW of England
Typically with turnover of £1m to £10m or 10 to 100 employees
Clients often in the construction sector, healthcare, accountants, lawyers and local councils.

Industry/Entity Type

Marketing

Font styles to use
Serif
Sans Serif

Colors
ec1f27

Requirements
Must have
• Consistent branding
• Logo in same place across all four reports
• Contact details in same place across all four reports
• Same font across all four reports
• Same colour across all four reports
• Professional and bold look
Nice to have
• Some strong stock photography
• 1 or 2 images per report
• More images for the 7-page report though
Should not have
• No graphics

```html
<!DOCTYPE html>
<html lang="en">
<head>
<meta charset="utf-8">
<title>10 Quick &amp; Easy Ways To Grow Your Business Using Social Media</title>
<link rel="stylesheet" href="https://fonts.googleapis.com/css2?family=Oswald:wght@600&family=Open+Sans:wght@400;700&display=swap">
<style>
  :root {
    --brand-red: #d7262e;
    --band-grey: #90979d;
    --ink: #3a3a3a;
    --rule: #4a4a4a;
    --muted: #5a5a5a;
    --paper: #ffffff;
  }
  * { margin: 0; padding: 0; box-sizing: border-box; }
  html, body { width: 848px; height: 1200px; overflow: hidden; background: var(--paper); }
  .page {
    position: relative;
    width: 848px;
    height: 1200px;
    background: var(--paper);
    color: var(--ink);
    font-family: "Open Sans", Arial, sans-serif;
    font-size: 15.6px;
    line-height: 23px;
  }
  .top-band { position: absolute; left: 0; top: 0; width: 848px; height: 18px; background: var(--band-grey); }
  .report-title {
    position: absolute; left: 54px; top: 86px; width: 745px;
    font-family: "Oswald", "Arial Narrow", sans-serif;
    font-weight: 600; font-size: 28.5px; line-height: 36px;
    color: var(--brand-red); letter-spacing: -0.2px; white-space: nowrap;
  }
  .step { position: absolute; left: 57px; width: 750px; }
  .step-heading { font-weight: 700; }
  .step-number { display: inline-block; width: 52px; }
  .step-point { margin-left: 52px; margin-top: 6px; width: 680px; }
  .step-point + .step-point { margin-top: 3px; }
  .footer-rule { position: absolute; left: 57px; top: 1021px; width: 736px; height: 2px; background: var(--rule); }
  .brand-lockup {
    position: absolute; left: 88px; top: 1040px; width: 92px; height: 122px;
    display: flex; flex-direction: column; align-items: center; gap: 8px;
    font-family: "Open Sans", Arial, sans-serif; font-weight: 700;
    font-size: 12.5px; line-height: 15px; text-align: center; color: var(--brand-red);
  }
  .brand-square { width: 58px; height: 58px; background: var(--brand-red); }
  .site-address { position: absolute; right: 57px; top: 1136px; font-size: 18px; color: var(--muted); }
</style>
</head>
<body>
<main class="page">
  <div class="top-band"></div>

  <h1 class="report-title">10 Quick &amp; Easy Ways To Grow Your Business Using Social Media</h1>

  <section class="step" style="top:150px">
    <p class="step-heading"><span class="step-number">1.</span>Decide what social media platforms to use for your business</p>
    <p class="step-point">(A).If you sell to other businesses, you will need to have a Company Profile on ProNet.</p>
    <p class="step-point">(B).If you sell to the public (consumers) you will almost certainly want to be on FriendSpace.</p>
    <p class="step-point">(C).Whether you are business-to-business (B2B) or business-to-consumer (B2C) you will also need to have a SearchCircle Page and a corporate ChirpFeed account.</p>
    <p class="step-point">(D).If your business lends itself to video having a corporate ClipStream account could also be very valuable.</p>
  </section>

  <section class="step" style="top:387px">
    <p class="step-heading"><span class="step-number">2.</span>Decide on what you want to achieve from social media.</p>
    <p class="step-point">(A).Set objectives that will help the business. Otherwise, you can end up doing social media for no discernable benefit.</p>
    <p class="step-point">(B).An example is to ‘increase the number of visitors to your website by 30% in the next 6 months’ or ‘drive sales via social media by £x p.a. by displaying y number of products p.m.’.</p>
  </section>

  <section class="step" style="top:547px">
    <p class="step-heading"><span class="step-number">3.</span>Decide on how you want your business to be seen on social media i.e. what’s your social media brand - formal, corporate, fun, provocative, educational or other?</p>
    <p class="step-point">(A).Ensure that your posts reflect your desired social media brand.</p>
  </section>

  <section class="step" style="top:642px">
    <p class="step-heading"><span class="step-number">4.</span>Decide on who will take a lead and ‘do your social media’.</p>
    <p class="step-point">(A).Typically, that can be someone in-house (if they have the skills) or someone from outside such as a freelancer or social media consultant (which avoids the risks and costs of employing someone specifically to do this work).</p>
  </section>

  <section class="step" style="top:753px">
    <p class="step-heading"><span class="step-number">5.</span>Commit to posting regularly.</p>
    <p class="step-point">(A).Results won’t necessarily come instantly and social media requires that ‘ you give before you get’.</p>
    <p class="step-point">(B).Start with 2 to 3 posts per week and work up to 1 per day.</p>
  </section>

  <section class="step" style="top:880px">
    <p class="step-heading" style="padding-left:52px;text-indent:-52px"><span class="step-number" style="text-indent:0">6.</span>Add links in your posts to certain pages of your website in order to drive traffic to your website to increase the likelihood of enquiries and/or sales.</p>
  </section>

  <div class="footer-rule"></div>

  <div class="brand-lockup">
    <span class="brand-square"></span>
    <span class="brand-name">Blue Harbour Marketing</span>
  </div>

  <p class="site-address">www.blueharbourmarketing.co.uk</p>
</main>
</body>
</html>
```